Business Card Design job - Tyre Shop

Client wants a double sided business cards designed for a Tyre Shop.

The logo can be used in multiple ways, some examples are attached.

The reference font is:
https://www.typebarrel.example/fonts/open-sans
Others can be applied.

Color scheme should be mainly black and white, and red as a third less used color.

Contact Information for Business Card

Required Fields (Portuguese language):
- Name "Artur Maldo"
- Title "Gerente"
- Phone "256 907 342"
- Website "www.rodalimpa.pt"
- Email "geral@rodalimpa.pt
- Address "Rua das Feiteiras N.187
4790-318 Quintela, Vizela"

Font styles to use
Sans Serif

Requirements
Must have
• Corporate Logo
Nice to have
• The client would like the card to have special feature to measure the tyre tread, as shown in examples attached.
• The tread Values as Portuguese law are:
• - Ilegal - less than 1.6mm
• - change tyres - between 3mm and 1.6 mm
• - OK - above 3mm
• Card should be kept standard rectangle size 85x55mm

```html
<!DOCTYPE html>
<html lang="pt">
<head>
<meta charset="utf-8">
<title>Roda Limpa — Cartão de visita</title>
<link href="https://fonts.googleapis.com/css2?family=Open+Sans:wght@400;600;700;800&display=swap" rel="stylesheet">
<style>
  :root {
    --ink: #111111;
    --card-black: #151515;
    --paper: #ffffff;
    --red: #e0201b;
    --grey-text: #555555;
    --stage: #e6e6e4;
    --ok: #27c22b;
    --warn: #e8d11a;
    --bad: #d8231e;
    --line: #bdbdbd;
  }
  * { box-sizing: border-box; margin: 0; padding: 0; }
  html, body { width: 1200px; height: 800px; overflow: hidden; }
  body {
    background: var(--stage);
    font-family: "Open Sans", Arial, sans-serif;
    display: flex;
    align-items: center;
    justify-content: center;
    gap: 40px;
  }
  .card {
    position: relative;
    width: 560px;
    height: 362px;
    overflow: hidden;
    box-shadow: 0 6px 18px rgba(0,0,0,.18);
  }

  /* Front */
  .card-front { background: var(--paper); }
  .front-brand {
    position: absolute; left: 30px; top: 26px;
    width: 300px;
    display: flex; align-items: center; justify-content: flex-end; gap: 8px;
    padding-bottom: 6px;
    border-bottom: 2px solid var(--red);
  }
  .brand-dot { width: 12px; height: 12px; border-radius: 50%; background: var(--ink); }
  .brand-name {
    font-weight: 800; font-size: 19px; letter-spacing: .5px;
    color: var(--ink); text-transform: uppercase;
  }
  .person { position: absolute; left: 50px; top: 112px; }
  .person-name { font-weight: 700; font-size: 24px; color: var(--ink); line-height: 1.1; }
  .person-title { font-size: 12px; color: var(--grey-text); }
  .contacts {
    position: absolute; left: 34px; top: 176px;
    list-style: none; font-size: 12.5px; color: var(--ink); line-height: 1.25;
  }
  .contacts li { display: flex; gap: 10px; margin-bottom: 6px; }
  .contacts .label { color: var(--red); font-weight: 700; width: 12px; }
  .front-panel {
    position: absolute; right: 0; top: 0;
    width: 220px; height: 100%;
    background: var(--card-black);
  }
  .front-tread {
    position: absolute; left: 30px; top: 36px;
    width: 170px; height: 230px;
    border-radius: 70% 30% 60% 40% / 40% 60% 40% 60%;
    background: linear-gradient(160deg, #f4f4f4, #c9c9c9);
  }
  .tagline {
    position: absolute; left: 0; right: 0; bottom: 26px;
    text-align: center; color: var(--paper);
    font-size: 8px; letter-spacing: 3px; text-transform: uppercase; line-height: 1.5;
  }

  /* Back */
  .card-back { background: linear-gradient(120deg, #1d1d1d, #0f0f0f); }
  .back-brand {
    position: absolute; left: 38px; top: 190px;
    transform: translateY(-50%) rotate(-90deg);
    transform-origin: left center;
    color: var(--paper); font-weight: 800; font-size: 30px;
    line-height: 1; text-transform: uppercase; white-space: nowrap;
    margin-left: 24px;
  }
  .back-tread {
    position: absolute; left: 110px; top: -20px;
    width: 250px; height: 330px;
    border-radius: 20% 80% 70% 30% / 15% 55% 45% 85%;
    background: linear-gradient(150deg, #f4f4f4, #c9c9c9);
  }
  .back-web {
    position: absolute; left: 372px; top: 170px;
    transform: rotate(-90deg); transform-origin: center;
    color: var(--paper); font-size: 13px; white-space: nowrap;
    width: 140px; margin-left: -70px; text-align: center;
  }
  .gauge { position: absolute; inset: 0; }
  .gauge text { font-family: "Open Sans", Arial, sans-serif; fill: var(--paper); font-size: 9px; }
</style>
</head>
<body>

<article class="card card-front" aria-label="Frente do cartão">
  <div class="front-brand">
    <span class="brand-dot"></span>
    <span class="brand-name">Roda Limpa</span>
  </div>
  <div class="person">
    <p class="person-name">Artur Maldo</p>
    <p class="person-title">Gerente</p>
  </div>
  <ul class="contacts">
    <li><span class="label">t:</span><span>256 907 342</span></li>
    <li><span class="label">e:</span><span>geral@rodalimpa.pt</span></li>
    <li><span class="label">a:</span><span>Rua das Feiteiras N.187<br>4790-318 Quintela, Vizela</span></li>
  </ul>
  <div class="front-panel">
    <div class="front-tread" role="img" aria-label="Ilustração de rasto de pneu em branco"></div>
    <p class="tagline">Especialista em pneus<br>&amp;<br>manutenção automóvel</p>
  </div>
</article>

<article class="card card-back" aria-label="Verso do cartão">
  <div class="back-tread" role="img" aria-label="Ilustração grande de rasto de pneu em branco"></div>
  <p class="back-brand">Roda Limpa</p>
  <p class="back-web">www.rodalimpa.pt</p>
  <svg class="gauge" width="560" height="362" viewBox="0 0 560 362" aria-label="Medidor de profundidade do piso">
    <line x1="505" y1="0" x2="505" y2="362" stroke="var(--line)" stroke-width="1"/>
    <!-- 8.0 ok -->
    <line x1="505" y1="42" x2="560" y2="42" stroke="var(--ok)" stroke-width="1.5"/>
    <path d="M478 38 l4 5 l8 -10" fill="none" stroke="var(--ok)" stroke-width="2"/>
    <text x="498" y="46" transform="rotate(-90 498 46)">8.0</text>
    <text x="498" y="170" transform="rotate(-90 498 170)">mm</text>
    <!-- 3.0 change -->
    <line x1="430" y1="262" x2="505" y2="262" stroke="var(--warn)" stroke-width="1.2" stroke-dasharray="4 3"/>
    <path d="M418 250 l10 18 h-20 z" fill="none" stroke="var(--warn)" stroke-width="1.6"/>
    <text x="470" y="272" transform="rotate(-90 470 272)">&lt;3.0</text>
    <text x="404" y="268" transform="rotate(-90 404 268)">trocar</text>
    <!-- 1.6 illegal -->
    <line x1="430" y1="292" x2="505" y2="292" stroke="var(--bad)" stroke-width="1.2" stroke-dasharray="4 3"/>
    <path d="M418 280 l10 18 h-20 z" fill="none" stroke="var(--bad)" stroke-width="1.6"/>
    <text x="470" y="304" transform="rotate(-90 470 304)">&lt;1.6</text>
    <text x="404" y="304" transform="rotate(-90 404 304)">ilegal</text>
  </svg>
</article>

</body>
</html>
```